Personal Development Model Graphic

I am creating a Personal Development/Coaching business and website and need some assistance with the development of a graphic that represents my methodology. I have already done what I consider to be a working version, but now it's time to have a professional design eye take a look at it and improve.

Specifically, I need assistance on color usage. I'd like each of the 8 areas of the model to have a color, and I've tried to utilize colors I feel are representative of the specific area(for example, purple for spirituality) but it doesn't really work for everything and perhaps additional thought could be put to that aspect of it.

Also, the model needs to work in reverse of the way it's pictured in the attached JPEG. So Friends needs to be first (top center)and then going clockwise, Spirituality needs to be in the 1:00 position not the 11:00 position and then continue around to Community, Family, Exercise, Career, Art/Creativity, and last at 11:00 Sexuality. I was going to update it before uploading, but I'm having trouble with Photoshop and just decided to pull the trigger on having a designer do it.

Thank you in advance for your creativity and ideas!

Industry/Entity Type

Business

Requirements
Nice to have
• It would be fantastic if it could feel modern, and high tech. I realize this is difficult with circles! But whatever you can do.

On color usage, it would again be wonderful to have colors that are more modern than traditional. I'll leave that to your discretion.

```html
<!DOCTYPE html>
<html lang="en">
<head>
<meta charset="utf-8">
<title>Working Title – Happiness Model</title>
<link rel="stylesheet" href="https://fonts.googleapis.com/css2?family=Bebas+Neue&display=swap">
<style>
  :root {
    --page: #ffffff;
    --paper: #f7f0dd;
    --grid: #ece2c8;
    --margin-line: #a9a9a9;
    --ribbon: #74a8ac;
    --ribbon-dark: #1f5d63;
    --text: #ffffff;
    --happiness: #dcc07a;
    --friends: #6d7a90;
    --spirituality: #6a5d6c;
    --community: #914352;
    --family: #bc7c66;
    --exercise: #b09c76;
    --career: #97938a;
    --art: #5b7a74;
    --sexuality: #6a7357;
  }
  * { margin: 0; padding: 0; box-sizing: border-box; }
  html, body { width: 1070px; height: 1200px; overflow: hidden; background: var(--page); }
  .canvas { position: relative; width: 1070px; height: 1200px; font-family: 'Bebas Neue', sans-serif; }
  .paper {
    position: absolute; left: 46px; top: 40px; width: 974px; height: 1122px;
    background-color: var(--paper);
    background-image:
      linear-gradient(var(--grid) 2px, transparent 2px),
      linear-gradient(90deg, var(--grid) 2px, transparent 2px);
    background-size: 117px 117px;
    background-position: 90px 10px;
  }
  .margin-line { position: absolute; left: 135px; top: 0; width: 3px; height: 1200px; background: var(--margin-line); }
  .ribbon { position: absolute; left: 74px; top: 84px; width: 592px; height: 132px; }
  .ribbon-title {
    position: absolute; left: 148px; top: 100px; font-size: 76px; line-height: 80px;
    color: var(--text); letter-spacing: 1px; text-shadow: 2px 3px 3px rgba(0,0,0,.35);
  }
  .area {
    position: absolute; border-radius: 50%; display: flex; align-items: center; justify-content: center;
    text-align: center; color: var(--text); font-size: 38px; line-height: 34px;
    text-shadow: 2px 2px 3px rgba(0,0,0,.45);
    box-shadow: 3px 5px 8px rgba(0,0,0,.35);
    width: 174px; height: 174px;
  }
  .area--center { width: 328px; height: 328px; font-size: 80px; left: 411px; top: 496px; background: var(--happiness); }
  .area--friends { left: 481px; top: 275px; background: var(--friends); }
  .area--spirituality { left: 703px; top: 371px; background: var(--spirituality); }
  .area--community { left: 783px; top: 569px; background: var(--community); }
  .area--family { left: 702px; top: 781px; background: var(--family); }
  .area--exercise { left: 487px; top: 876px; background: var(--exercise); }
  .area--career { left: 263px; top: 779px; background: var(--career); }
  .area--art { left: 183px; top: 581px; background: var(--art); }
  .area--sexuality { left: 264px; top: 370px; background: var(--sexuality); }
</style>
</head>
<body>
  <main class="canvas">
    <div class="paper"></div>
    <div class="margin-line"></div>

    <svg class="ribbon" viewBox="0 0 592 132" aria-hidden="true">
      <polygon points="0,34 46,34 78,132 30,126" fill="var(--ribbon-dark)"/>
      <polygon points="46,100 78,132 78,100" fill="#143f43"/>
      <polygon points="42,0 548,0 590,54 548,110 42,110" fill="var(--ribbon)"/>
    </svg>
    <h1 class="ribbon-title">Working Title</h1>

    <div class="area area--center">Happiness</div>
    <div class="area area--friends">Friends</div>
    <div class="area area--spirituality">Spirituality</div>
    <div class="area area--community">Community</div>
    <div class="area area--family">Family</div>
    <div class="area area--exercise">Exercise</div>
    <div class="area area--career">Career</div>
    <div class="area area--art">Art&amp;<br>Creativity</div>
    <div class="area area--sexuality">Sexuality</div>
  </main>
</body>
</html>
```